Medical Practice and Business Coaching Website Design

I need a professional website designed for a medical business, TVD Medical.
The website will be hosted on Vemora (similar design functionality as PLYX).

About the website:
Pages for the website:
- Home page (a brief overview of the company with a section for "Ultrasound Clinics" and "Coaching and Courses" that link to these pages with all the info and packages for these sections)
- About Us (section for company info and info about Melinda Ashcombe, founder and business coach)
- Ultrasound Clinics (all the info about ultrasound, our packages, links to book, gallery of 3D/4D images, FAQs, social media links)
- Coaching and Courses (All of our coaching package info, course info with a waiting list sign up, section for free business download resources, social media links, blog posts)
- Contact Us (info for our corrowen ultrasound location and bookings with a map, contact form, email and phone details)

Pages that are also needed but not visible in the top menu:
- Blog Page
- Waiting List Page x2 (Dubbo pop-up 3D clinic, Online Course)
- Thanks for subscribing page

We have a company logo and a logo for both the ultrasound clinics and the Coaching sides of the business. They are attached as well as the HEX codes for the branding colours. Ideally the company areas of the site will be in the blue, purple and teal colours. The ultrasound clinics page will be mostly in the purple with the "clinics" logo featuring on the page.
The courses and coaching page will be dominant in the blue branding colours with accents of purple and teal. The courses logo will be somewhere on the page too.

About our company:
Our company has 2 separate businesses which will have their own pages on the website.
We have a medical imaging business which specialises in ultrasound. We have 3 locations/services:
- Corrowen Ultrasound: open Fridays and the occasional saturday. Our main focus and where the focus on the clinical page needs to be.
- Tarlee Flats Ultrasound: Currently closed, no re-opening date and unlikely to reopen.
- Pop-up clinics: most commonly occur in Dubbo. occasionally in Parkes. Dates for next pop-up will be announced in the future.

Our Blayney practice offers both diagnostic ultrasound (referral from doctor) for all areas of the body and 3d/4d pregnancy ultrasounds for entertainment purposes.
The content for the ultrasound clinics part of the website can be found on the current corrowen ultrasound website: corrowenscans.com.au
This website will be replaced by the new company site. All of the info on this site will end up on the clinics page of the new company website.

The second part of the company is a coaching and courses service for medical professionals who want to start or grow their business.
We currently have coaching packages for 1-on-1 online advice and guidance.

Coaching: all take place on Wavo and can be recorded for them to watch again after. Notes, documents and links that are discussed are provided after session

- FREE 15 minute session: discuss current business or business idea, if and how I can help and potential things they can do. One per client

- Single Coaching Session - 1hr with Melinda

- Silver coaching package: 1 x 1hr Coaching Call with Melinda
Unlimited Email with Melinda for 1 month
Access to our Private Chatterly Group to network with other medical professionals and business owners

- Silver Coaching Package With Social Media Management:
As above with 1 month Social Media Management (15 posts, Chatterly and Pictoreel)

- Gold coaching package: 2 x 1hr Coaching Calls with Melinda
Access to our Private Chatterly

- Gold Coaching Package With Social Media Management:

- Business Buddy Package: Unlimited Coaching Calls
Unlimited SMS
Unlimited Emails
Social Media Management (Chatterly and Pictoreel, 1 post per day) Valued at over $700
Business Workshop Hour (something different each month...social media, medicare, website, branding, live events, etc)

Enrollment for our first course opens in May and clients can join the waitlist in the meantime.
Course is aimed at medical professionals who want to grow their patient numbers and create an online presence for their business.
Ideal for: small practices where the owner does everything, not necessarily familiar with marketing/social media/websites, goes to the very basics and steps through everything in getting a logo, branding, website, building social media pages, creating content.

Course name to come but it will be something like "helpful marketing in healthcare" or "the business of healthcare"

We will also have a blog on the website and a podcast (in the future).

I would like a testimonial on at least the clinics page and the coaching page. Here is one for each but I have more if need be:
Coaching: "I knew I wanted to start my own business but I had no idea where to begin. It would have been easy to abort my dreams of starting my own business had it not been for the direction and unwavering support of Melinda from TVD medical. Melinda dissected the process into manageable bit sized pieces for me and worked tirelessly behind the scenes ensuring everything was on track. Her friendly, warm and approachable manner
equated to more than her just being my business coach, she has now become a friend.
Thank you!!"

Ultrasound testimonial: "Amazing service! Best ultrasound experience I’ve had. Super friendly and informative staff. Great technology. If I didn’t live so far away I’d go to Blayney for all my ultrasounds!"

I would also like a section for a welcome video (yet to be recorded) on the home page, ultrasound clinics page and coaching/courses page.

I've attached the company logo and the sub-logos in different formats. There is also a head shot of Melinda for the about us page, an image of Melinda with a coaching client for the coaching page and multiple 3D ultrasound images for the gallery on the clinics page.

Target Market(s)

Mostly targeted at medical professionals. Pregnant women and anyone needing an ultrasound are the targets for the clinics page

Industry/Entity Type

Healthcare

Number of Pages Required

5+ page

Colors
0054AA
0677BA
7BADD7
CADEEF
E8F1F8
0094D4
00A9DD
6FCCEA
C7EBF8
E9F6FB
00AB8E
00BBA5
67D7C9
C6EFE9
E9F9F6
A7469A
B969AE
D3A5CF
EDDBEB
F8F0F9
6B429C
8869AF
B7A5CE
E3DAEB
F3F0F8

```html
<!DOCTYPE html>
<html lang="en">
<head>
<meta charset="utf-8">
<title>TVD Medical</title>
<link href="https://fonts.googleapis.com/css2?family=Poppins:wght@400;500;600;700&display=swap" rel="stylesheet">
<style>
:root{
  --teal:#2fa9ab;
  --purple:#7b5ea7;
  --purple-deep:#4b2f83;
  --navy-arrow:#3e3b7c;
  --ink:#222222;
  --text:#3a3a3a;
  --muted:#6b6b6b;
  --white:#ffffff;
  --plane-area:#8a70b2;
}
*{box-sizing:border-box;margin:0;padding:0}
html,body{width:1200px;height:2565px;overflow:hidden}
body{font-family:'Poppins',sans-serif;background:var(--white);color:var(--text);position:relative}
a{color:inherit;text-decoration:none}

/* header */
.site-header{position:absolute;left:0;top:0;width:1200px;height:95px;background:var(--white)}
.brand{position:absolute;left:112px;top:24px;display:flex;align-items:center;gap:8px;font-size:17px;font-weight:600;color:var(--purple-deep)}
.brand-dot{width:40px;height:40px;border-radius:50%;border:3px solid var(--teal)}
.main-nav{position:absolute;right:107px;top:37px;display:flex;gap:33px;font-size:15px;color:var(--ink)}
.main-nav .active{color:var(--teal)}

/* hero */
.hero{position:absolute;left:0;top:95px;width:1200px;height:645px;background:linear-gradient(100deg,#33414f 0%,#2c3a47 45%,#3a4652 70%,#2a3340 100%)}
.hero-title{position:absolute;left:108px;top:188px;font-size:58px;font-weight:700;color:var(--white);line-height:1}
.hero-text{position:absolute;left:112px;top:270px;width:492px;font-size:15.5px;line-height:32px;color:var(--white)}
.btn{position:absolute;display:flex;align-items:center;justify-content:center;width:206px;height:56px;background:var(--teal);color:var(--white);font-size:15px;font-weight:600;border-radius:4px;box-shadow:0 6px 12px rgba(0,0,0,.15)}
.hero .btn{left:112px;top:393px}
.hero-photo{position:absolute;left:636px;top:82px;width:456px;height:481px;background:linear-gradient(160deg,#e9e6e3 0%,#d98a7a 35%,#f1ede7 60%,#b07a5e 100%)}
.slider-arrow{position:absolute;top:295px;width:58px;height:57px;background:var(--navy-arrow);display:flex;align-items:center;justify-content:center}
.slider-arrow.prev{left:20px}
.slider-arrow.next{left:1127px}

/* ultrasound */
.clinic-media{position:absolute;left:80px;top:840px}
.clinic-title{position:absolute;left:604px;top:915px;font-size:44px;font-weight:700;color:var(--ink);line-height:1.1}
.clinic-text{position:absolute;left:602px;top:987px;width:490px;font-size:14px;line-height:28.5px;color:var(--muted)}
.clinic-text p+p{margin-top:17px}
.clinics .btn{left:602px;top:1199px}

/* coaching */
.coaching{position:absolute;left:0;top:1472px;width:1200px;height:532px;background:linear-gradient(100deg,#e9ebed 0%,#f4f5f6 35%,#f6f7f8 70%,#eef0f1 100%)}
.coaching-title{position:absolute;left:0;top:72px;width:1200px;text-align:center;font-size:34px;font-weight:600;color:var(--teal)}
.coaching-sub{position:absolute;left:290px;top:130px;width:620px;text-align:center;font-size:15px;line-height:32px;color:var(--ink)}
.rule{position:absolute;left:570px;top:213px;width:66px;height:3px;background:var(--purple-deep)}
.coaching-text{position:absolute;left:110px;top:240px;width:980px;text-align:center;font-size:14.3px;line-height:32px;color:#7a7a7a}
.coaching .btn{left:499px;top:393px}

/* subscribe */
.subscribe{position:absolute;left:0;top:2004px;width:1200px;height:226px;background:var(--purple)}
.subscribe-title{position:absolute;left:110px;top:52px;font-size:44px;font-weight:600;line-height:57px;color:var(--white)}
.plane-slot{position:absolute;left:387px;top:53px;width:136px;height:120px;background:var(--plane-area);border-radius:4px}
.field{position:absolute;top:92px;width:235px;height:38px;border-bottom:1.5px solid rgba(255,255,255,.85);font-size:15px;color:var(--white)}
.field.email{left:555px}
.field.name{left:813px}
.submit{position:absolute;left:1068px;top:95px}

/* footer */
.footer-col{position:absolute;top:2302px}
.footer-col h3{font-size:19px;font-weight:500;color:var(--ink);margin-bottom:16px}
.footer-col ul{list-style:none;font-size:14px;line-height:29.4px;color:var(--text)}
.connect{left:188px;width:340px}
.connect p{font-size:14px;line-height:29.4px;color:var(--text)}
.social{display:flex;gap:14px;margin-top:18px;font-size:13px;color:var(--ink)}
.resources{left:725px}
.help{left:947px}
.copyright{position:absolute;left:0;top:2524px;width:1200px;text-align:center;font-size:15px;color:var(--ink)}
</style>
</head>
<body>

<header class="site-header">
  <div class="brand"><span class="brand-dot"></span>TVD Medical</div>
  <nav class="main-nav">
    <a class="active">Home</a><a>About</a><a>Ultrasound Clinics</a><a>Coaching and Courses</a><a>Contact Us</a>
  </nav>
</header>

<section class="hero">
  <h1 class="hero-title">TVD Medical</h1>
  <p class="hero-text">Lorem ipsum dolor sit amet, consectetur adipiscing elit, sed do eiusmod tempor incididunt ut labore et dolore magna aliqua.<br>Ut enim ad minim veniam,</p>
  <a class="btn">Get Started</a>
  <div class="hero-photo" role="img" aria-label="Photo of two women in an ultrasound clinic beside a scanning machine"></div>
  <a class="slider-arrow prev"><svg width="14" height="20" viewBox="0 0 14 20"><path d="M10 3 3 10l7 7" fill="none" stroke="#fff" stroke-width="2.4"/></svg></a>
  <a class="slider-arrow next"><svg width="14" height="20" viewBox="0 0 14 20"><path d="M4 3l7 7-7 7" fill="none" stroke="#fff" stroke-width="2.4"/></svg></a>
</section>

<section class="clinics">
  <svg class="clinic-media" width="500" height="540" viewBox="0 0 500 540">
    <path d="M5 50 V520 C150 505 300 515 457 530 V490" fill="none" stroke="#2fa9ab" stroke-width="1.2"/>
    <defs><linearGradient id="scanTones" x1="0" y1="0" x2="1" y2="1">
      <stop offset="0" stop-color="#d8dde2"/><stop offset=".45" stop-color="#9aa6b2"/><stop offset="1" stop-color="#eceff1"/>
    </linearGradient></defs>
    <path d="M14 12 C150 4 330 10 482 18 V488 C330 478 150 478 14 488 Z" fill="url(#scanTones)" role="img" aria-label="Photo of a sonographer scanning a pregnant patient with an ultrasound monitor"/>
  </svg>
  <h2 class="clinic-title">Ultrasound Clinics</h2>
  <div class="clinic-text">
    <p>Lorem ipsum dolor sit amet, consectetur adipiscing elit, sed do eiusmod tempor incididunt ut labore et dolore magna aliqua. Ut enim ad minim veniam, quis nostrud exercitation ullamco laboris</p>
    <p>Lorem ipsum dolor sit amet, consectetur adipiscing elit, sed do eiusmod tempor incididunt ut labore et dolore magna aliqua. Ut enim ad minim veniam, quis nostrud exercitation ullamco laboris</p>
  </div>
  <a class="btn">Read More</a>
</section>

<section class="coaching" role="img" aria-label="Faint background photo of a doctor at a desk with a laptop and stethoscope">
  <h2 class="coaching-title">Coaching and Courses</h2>
  <p class="coaching-sub">All take place on Wavo and can be recorded for them to watch again after. Notes, documents and links that are discussed are provided after session</p>
  <span class="rule"></span>
  <p class="coaching-text">Lorem ipsum dolor sit amet, consectetur adipiscing elit, sed do eiusmod tempor incididunt ut labore et dolore magna aliqua. Ut enim ad minim veniam, quis nostrud exercitation ullamco laboris nisi ut aliquip ex ea commodo consequat. Duis aute irure dolor in reprehenderit in voluptate velit esse cillum dolore eu fugiat nulla pariatur. Excepteur sint occaecat cupidatat non proident, sunt in<br>culpa qui officia deserunt mollit anim id est laborum</p>
  <a class="btn">View More &rarr;</a>
</section>

<section class="subscribe">
  <h2 class="subscribe-title">Thanks for<br>subscribing</h2>
  <div class="plane-slot" role="img" aria-label="Outline illustration of a paper plane"></div>
  <div class="field email">Email</div>
  <div class="field name">Name</div>
  <svg class="submit" width="26" height="14" viewBox="0 0 26 14"><path d="M1 7h22M17 2l6 5-6 5" fill="none" stroke="#fff" stroke-width="2.2"/></svg>
</section>

<footer>
  <div class="footer-col connect">
    <h3>Connect</h3>
    <p>1900,Lorem ipsum dolor sit amet, consectetur adipiscing elit,</p>
    <div class="social"><span>Chatterly</span><span>Pictoreel</span><span>Chirpline</span></div>
  </div>
  <div class="footer-col resources">
    <h3>Resources</h3>
    <ul><li>Home</li><li>About</li><li>Ultrasound Clinics</li><li>Coaching and Courses</li><li>Contact</li></ul>
  </div>
  <div class="footer-col help">
    <h3>Help Us</h3>
    <ul><li>Support</li><li>FAQ</li><li>Blog</li></ul>
  </div>
  <p class="copyright">&copy; 2022 All Rights Reserved</p>
</footer>

</body>
</html>
```